Pool Builder Website Design in arizona

Our current site is located here: tidemoor.net

We are looking to give this a modern facelift. We will be cutting your design into a wordpress theme so we can utilize the CMS plateform backend.

Look and Feel
• Clean cut and professional
• Mobile friendly
• Updated from old site
• Feel intrigued but relax (do you have trust logos? Odile looking into this)
Colors
• Warm tropical neutral colors
• Orange, brown, blues
- Please make the site modern and more sleek look that looks like a 2015 style design and NOT 1999.
- Must be coded as a wordpress theme
- must create a home page, inner page and blog page
- must allow client to BLOG using the post section in wordpress

This pool company is a pool builder/installer in Phoenix arizona.

NOTE::: Please create a home page and one internal page.

Industry/Entity Type

Builder

Coding

Coded - Design and coding required

Number of Pages Required

3 page

Font styles to use
Serif
Sans Serif

Requirements
Must have
• - Must be coded as a wordpress theme
• - must create a home page, inner page and blog page
• - must allow client to BLOG using the post section in wordpress

```html
<!DOCTYPE html>
<html lang="en">
<head>
<meta charset="utf-8">
<title>Coralline Pools — Fiberglass Pool Experts</title>
<link href="https://fonts.googleapis.com/css2?family=Arimo:wght@400;700&family=Open+Sans:ital,wght@0,400;0,600;1,400;1,600&display=swap" rel="stylesheet">
<style>
:root{
  --blue:#1f6fd6;
  --blue-deep:#1c4f9c;
  --blue-light:#3a8eea;
  --green:#6ebf4b;
  --green-dark:#2f7d1c;
  --orange:#d9460b;
  --charcoal:#2b2b2b;
  --charcoal-2:#333333;
  --footer-bottom:#3a3a3a;
  --beige:#ece8e1;
  --white:#ffffff;
  --text:#4a4a4a;
  --muted:#9a9a9a;
  --teal-link:#4fc0b0;
}
*{margin:0;padding:0;box-sizing:border-box}
html,body{width:878px;height:1200px;overflow:hidden;background:var(--beige)}
body{font-family:"Arimo",Arial,sans-serif;color:var(--text)}
.page{position:relative;width:878px;height:1200px;overflow:hidden}
.abs{position:absolute}

/* hero */
.hero-photo{left:0;top:0;width:878px;height:356px;
  background:linear-gradient(160deg,#7a8f7a 0%,#8fb0b8 18%,#4fb4d8 40%,#5cc6e6 65%,#8fd6ea 100%)}
.site-header{left:0;top:0;width:878px;height:66px;
  background:linear-gradient(#2a7ce0,#1b63c6);border-bottom:1px solid #5e9ee8}
.main-nav a{position:absolute;top:0;height:66px;line-height:68px;color:var(--white);
  font-family:"Arimo",sans-serif;font-size:12px;text-decoration:none;transform:translateX(-50%)}
.main-nav a.active{background:var(--blue-light);width:74px;text-align:center}
.brand{left:137px;top:0;width:110px;height:103px;background:var(--green);
  clip-path:polygon(0 0,100% 0,100% 100%,50% 82%,0 100%)}
.brand-inner{position:absolute;left:7px;top:5px;width:96px;height:62px;background:var(--white);
  display:flex;align-items:center;justify-content:center;text-align:center;
  font-family:"Arimo",sans-serif;font-weight:700;font-size:14px;line-height:15px;color:var(--blue-deep)}
.hero-tag{left:406px;height:35px;color:var(--white);font-family:"Arimo",sans-serif;padding-left:18px;white-space:nowrap}
.tag-name{top:183px;width:224px;background:var(--green);font-size:23px;line-height:36px}
.tag-title{top:225px;width:358px;height:32px;background:var(--blue-deep);font-size:23px;line-height:33px}
.tag-copy{top:264px;width:389px;height:47px;background:var(--orange);font-size:12.5px;font-weight:700;
  line-height:16px;padding-top:8px;padding-right:14px;white-space:normal;letter-spacing:.3px}

/* category band */
.category-band{left:0;top:356px;width:878px;height:56px;background:var(--green)}
.progress{left:137px;top:360px;width:603px;height:4px;background:var(--green-dark)}
.progress span{position:absolute;left:6px;top:0;width:111px;height:4px;background:var(--white)}
.category-tabs a{position:absolute;top:380px;color:var(--white);font-family:"Open Sans",sans-serif;
  font-size:11px;text-decoration:none;transform:translateX(-50%);white-space:nowrap}

/* carousel */
.carousel{left:0;top:412px;width:878px;height:144px;background:var(--charcoal)}
.slide{top:430px;width:166px;height:100px}
.slide-1{left:177px;background:linear-gradient(135deg,#3aa6d8,#7fd0ec)}
.slide-2{left:354px;background:linear-gradient(135deg,#c98d6a,#e8c3a0 60%,#9ac8e0)}
.slide-3{left:531px;background:linear-gradient(180deg,#4ea6dc,#8fd0ee 70%,#d7c9a6)}
.arrow{top:474px;color:var(--white);font-size:18px;font-family:"Arimo",sans-serif}

/* intro */
.intro-card{left:138px;top:583px;width:596px;height:212px;background:var(--white)}
.intro-title{left:145px;top:590px;font-size:17.5px;font-weight:400;color:#111}
.intro-text{left:144px;top:614px;width:270px;font-size:7.6px;line-height:12px;color:#555}
.intro-text p+p{margin-top:11px;text-indent:6px}
.video{left:424px;top:599px;width:302px;height:169px;background:#1c1c1c}
.video-title{left:8px;top:6px;font-size:8.5px;font-weight:700;color:var(--white)}
.video-icons{right:6px;top:6px;display:flex;gap:5px}
.video-icons i{display:block;width:9px;height:9px;border-radius:50%;background:#cfcfcf}
.video-frame{left:6px;top:20px;width:290px;height:120px;background:linear-gradient(135deg,#2d8ab0,#47aacc 50%,#2a7aa3)}
.play{left:125px;top:47px;width:42px;height:30px;border-radius:6px;background:rgba(30,30,30,.75)}
.controls{left:6px;top:142px;width:290px;height:22px}
.ctrl{top:0;height:22px;background:#2a2a2a}
.time{top:6px;font-size:6.5px;color:#ccc}

.divider{left:144px;top:805px;width:590px;height:1px;background:#cfcac2}

/* feature boxes */
.box{top:821px;height:116px;color:var(--white)}
.box-install{left:144px;width:138px;background:var(--green);padding:17px 8px 17px 9px}
.box-testimonials{left:295px;width:138px;background:var(--blue-deep);padding:19px 10px}
.box-blog{left:445px;width:289px;background:var(--orange);padding:19px 11px}
.box h3{font-weight:400;font-size:9.5px;margin-bottom:7px;white-space:nowrap}
.box-testimonials h3,.box-blog h3{font-size:8px;text-transform:uppercase}
.box-blog h3{font-weight:700;margin-bottom:11px}
.box p{font-size:7.5px;line-height:10px}
.box-install p{padding-left:1px}
.post{display:flex;gap:6px;margin-bottom:9px;align-items:flex-start}
.post-date{width:22px;height:22px;background:#1a1a1a;font-size:7px;line-height:7.5px;text-align:center;padding-top:3px;flex:none}
.post strong{display:block;font-size:8.5px;margin-bottom:1px}
.post span{font-size:7px}

/* footer */
.site-footer{left:0;top:977px;width:878px;height:168px;background:var(--charcoal-2)}
.footer-title{top:1007px;font-size:8.5px;color:var(--muted);text-transform:uppercase}
.footer-text{font-family:"Open Sans",sans-serif;font-style:italic;font-size:7px;line-height:11.3px;color:#9a9a9a}
.footer-text a{color:var(--teal-link);text-decoration:none}
.tweet-time{display:block;margin:4px 0 8px;color:#aaa}
.social{left:552px;top:1027px;display:flex;gap:5px}
.social span{display:block;width:23px;height:21px;background:#474747}
.newsletter{left:553px;top:1057px;width:157px;height:22px;display:flex}
.newsletter div{flex:1;background:#474747;font-family:"Open Sans",sans-serif;font-style:italic;font-size:7px;color:#8a8a8a;line-height:22px;padding-left:8px}
.newsletter b{width:23px;background:#8a8a8a;color:var(--white);text-align:center;line-height:22px;font-size:10px}
.footer-bar{left:0;top:1145px;width:878px;height:55px;background:var(--footer-bottom)}
.copyright{left:143px;top:1167px;font-size:7px;color:#999}
.footer-links{right:169px;top:1167px;font-size:7px;color:#aaa;word-spacing:2px}
.footer-links em{font-style:normal;margin:0 8px}
</style>
</head>
<body>
<div class="page">

  <div class="abs hero-photo" role="img" aria-label="Photo of a curved backyard swimming pool with tiled steps, flower beds and lounge chairs"></div>

  <header class="abs site-header">
    <nav class="main-nav">
      <a class="active" href="#" style="left:326px">Style</a>
      <a href="#" style="left:412px">Portfolio</a>
      <a href="#" style="left:514px">Installation</a>
      <a href="#" style="left:617px">About us</a>
      <a href="#" style="left:714px">Contact</a>
    </nav>
  </header>

  <div class="abs brand"><div class="brand-inner">Coralline<br>Pools</div></div>

  <div class="abs hero-tag tag-name">Coralline Pools</div>
  <div class="abs hero-tag tag-title">the fiberglass pool experts !</div>
  <div class="abs hero-tag tag-copy">A Phoenix fiberglass pool is more than just a relaxing piece of heaven, it is an investment.</div>

  <div class="abs category-band"></div>
  <div class="abs progress"><span></span></div>
  <nav class="category-tabs">
    <a href="#" style="left:191px">Fiberglass Pools</a>
    <a href="#" style="left:316px">Fiberglass Spools</a>
    <a href="#" style="left:434px">Fiberglass Spas</a>
    <a href="#" style="left:548px">Custom Beehives</a>
    <a href="#" style="left:680px">Custom Water Features</a>
  </nav>

  <section class="abs carousel"></section>
  <div class="abs slide slide-1" role="img" aria-label="Photo of a child swimming underwater in goggles"></div>
  <div class="abs slide slide-2" role="img" aria-label="Photo of a group of friends smiling by the pool"></div>
  <div class="abs slide slide-3" role="img" aria-label="Photo of a girl sitting at the edge of a pool"></div>
  <div class="abs arrow" style="left:144px">&#8249;</div>
  <div class="abs arrow" style="left:727px">&#8250;</div>

  <section class="abs intro-card"></section>
  <h1 class="abs intro-title">A Phoenix fiberglass pool is</h1>
  <div class="abs intro-text">
    <p>&nbsp;A Phoenix fiberglass pool is more than just a relaxing piece of heaven, it is an investment.&nbsp; Why spend your money on a pool that requires more maintenance and scratches your feet when you can enjoy the smooth feeling of fiberglass on your toes?&nbsp; Fiberglass pools offer many unique advantages over concrete pools, and Coralline Pools are the premier AZ fiberglass pool builders.</p>
    <p>We also offer many other products and services to enhance your yard and increase the value of your home. Check out some of our cost effective and sensuous fiberglass spools and spas, our beautiful and calming custom water features, or our fun custom beehives, firepits, and barbe-cues.&nbsp; Our fiberglass pools come in many sizes and styles and installation is a breeze.&nbsp; Call or stop in today to see how we can make your yard "A small bit of paradise"! We are the best arizona pool builder.</p>
  </div>

  <div class="abs video">
    <div class="abs video-title">Selected Video Name</div>
    <div class="abs video-icons"><i></i><i></i><i></i><i></i></div>
    <div class="abs video-frame" role="img" aria-label="Video still of people floating on inner tubes in a pool">
      <svg class="abs play" viewBox="0 0 42 30"><polygon points="17,8 28,15 17,22" fill="#fff"/></svg>
    </div>
    <div class="abs controls">
      <div class="abs ctrl" style="left:0;width:46px"><svg width="46" height="22"><rect x="19" y="6" width="3" height="10" fill="#ddd"/><rect x="24" y="6" width="3" height="10" fill="#ddd"/></svg></div>
      <div class="abs ctrl" style="left:49px;width:192px">
        <span class="abs time" style="left:8px">01:46</span>
        <svg class="abs" style="left:30px;top:9px" width="132" height="4"><rect width="132" height="4" rx="2" fill="#555"/><rect width="36" height="4" rx="2" fill="#e6e6e6"/></svg>
        <span class="abs time" style="right:8px">02:28</span>
      </div>
      <div class="abs ctrl" style="left:244px;width:22px"><svg width="22" height="22"><rect x="6" y="6" width="10" height="10" fill="none" stroke="#ddd"/></svg></div>
      <div class="abs ctrl" style="left:268px;width:22px"><svg width="22" height="22"><polygon points="6,9 9,9 13,6 13,16 9,13 6,13" fill="#ddd"/></svg></div>
    </div>
  </div>

  <div class="abs divider"></div>

  <article class="abs box box-install">
    <h3>Fiberglass Pool Installation</h3>
    <p>Vivamus metus turpis, biben-dum vitae euismod vel, vulpu-tate vel nibh. Class aptent taciti sociosqu ad litora torquent per conubia nostra, per inceptos himenaeos. Donec erat sem,</p>
  </article>
  <article class="abs box box-testimonials">
    <h3>Testimonials</h3>
    <p>vel, vulputate vel nibh. Class aptent taciti sociosqu ad litora torquent per conubia nostra, per inceptos himenaeos. Donec erat sem, vehicula id dictum sit [...]</p>
    <p style="margin-top:3px">&nbsp;- Hal Brenner -</p>
  </article>
  <article class="abs box box-blog">
    <h3>Blog News</h3>
    <div class="post"><div class="post-date">Apr<br>01</div><div><strong>Nice &amp; clean. The best for you blog!</strong><span>Vivamus metus turpis, bibendum vitae euismod vel, vulputate vel</span></div></div>
    <div class="post"><div class="post-date">Apr<br>02</div><div><strong>Nice &amp; clean. The best for you blog!</strong><span>Vivamus metus turpis, bibendum vitae euismod vel, vulputate vel</span></div></div>
  </article>

  <footer class="abs site-footer"></footer>
  <div class="abs footer-title" style="left:171px">Text widget</div>
  <p class="abs footer-text" style="left:171px;top:1028px;width:157px;text-align:justify">Donec sed odio dui. Nulla vitae elit libero, a pharetra augue. Nullam id dolor id nibh ultricies vehicula ut id elit. Integer posuere erat a ante venenatis dapibus posuere velit aliquet. Duis mollis, est non commodo luctus, nisi erat porttitor ligula, eget lacinia odio sem nec elit.</p>

  <div class="abs footer-title" style="left:361px">Updates widget</div>
  <div class="abs footer-text" style="left:361px;top:1028px;width:165px">
    <a href="#">@marenvoss</a> Why thank you. Your work looks awesome by the way! <a href="#">@pinegrovestudio</a>
    <span class="tweet-time">19 days ago</span>
    <a href="#">@tobiasreel</a> You can seek a refund through the shop if it is not as advertised - but it is :)
    <span class="tweet-time">21 days ago</span>
  </div>

  <div class="abs footer-title" style="left:555px">Stay with us</div>
  <div class="abs social" aria-label="Social links">
    <span></span><span></span><span></span><span></span><span></span>
  </div>
  <div class="abs newsletter"><div>Enter email for newsletter</div><b>&#8250;</b></div>

  <div class="abs footer-bar"></div>
  <div class="abs copyright">Copyright 2015</div>
  <div class="abs footer-links">Style<em>/</em>Portfolio<em>/</em>Installation<em>/</em>About us<em>/</em>Contact</div>

</div>
</body>
</html>
```